Flyer for a Business Consultant

I need a one-page description of services. I am a Brinmore Accredited Talents Mentor. I do not have a personal website but think I will soon purchase this template https://quillerlayouts.example/layouts/lectern/. I like the larger font, simplicity and larger font. I will attach his pricing flyer which I like - not to overly guide or restrict your creative thinking, but only to give a little perspective. I don't like busy, noisy - I like clarity, simplicity. Here 's the Brinmore website which these same traits https://www.brinmoretalentshub.example/ and can be a source of ideas and colors.

Target Market(s)

CEOs and Middle Managers in organizations

Industry/Entity Type

Financial Service

Colors

Designer to choose colors to be used in the design.

Requirements
Must have
• Clarity, simplicity, but also strength (not weak or frilly looking)
Nice to have
• Warm color(s), larger/not skinny font
Should not have
• Loud, noisy, busy

```html
<!DOCTYPE html>
<html lang="en">
<head>
<meta charset="utf-8">
<title>Strength-Based Team Effectiveness</title>
<link href="https://fonts.googleapis.com/css2?family=PT+Sans:wght@400;700&family=PT+Sans+Narrow:wght@400;700&display=swap" rel="stylesheet">
<style>
  :root {
    --ink-white: #ffffff;
    --night: #0d1620;
    --dusk: #2a2420;
    --ember: #8a4a22;
    --col-light: #c0bcbc;
    --col-mid: #9a9696;
    --col-dark: #726b6b;
    --col-text: #333030;
    --footer: #e7ecb8;
    --footer-text: #6a6a6a;
    --badge: #7c8a60;
  }
  html, body { margin: 0; padding: 0; overflow: hidden; }
  body { width: 927px; height: 1200px; position: relative; background: var(--night); font-family: "PT Sans", sans-serif; }

  .hero { position: absolute; left: 0; top: 0; width: 927px; height: 780px; overflow: hidden; }
  .hero-scene {
    position: absolute; inset: 0;
    background:
      radial-gradient(ellipse 260px 120px at 468px 375px, rgba(255,220,150,0.95), rgba(232,145,58,0.55) 45%, rgba(232,145,58,0) 100%),
      linear-gradient(180deg, var(--night) 0%, #1a2430 28%, #4a3a30 42%, var(--ember) 50%, #3b2a22 58%, var(--dusk) 72%, #1a1614 100%);
  }
  .hero-title { position: absolute; left: 0; top: 0; width: 100%; text-align: center; color: var(--ink-white); margin: 0; font-weight: 400; }
  .hero-title .kicker { position: absolute; left: 0; right: 0; top: 84px; font-size: 41px; letter-spacing: 0.5px; }
  .hero-title .main { position: absolute; left: 0; right: 0; top: 143px; font-size: 58px; letter-spacing: 0.5px; }

  .promise { position: absolute; left: 0; top: 0; width: 100%; text-align: center; color: var(--ink-white); }
  .promise-heading { position: absolute; left: 0; right: 0; top: 560px; margin: 0; font-weight: 400; font-size: 40px; line-height: 52px; }
  .promise-list { position: absolute; left: 190px; width: 547px; top: 670px; margin: 0; padding: 0; list-style: none; font-family: "PT Sans Narrow", sans-serif; font-size: 17px; }
  .promise-list li { height: 30px; line-height: 30px; border-bottom: 1px solid rgba(255,255,255,0.25); }
  .promise-list li:last-child { border-bottom: none; }

  .services { position: absolute; left: 0; top: 780px; width: 927px; height: 290px; display: flex; }
  .service { height: 100%; box-sizing: border-box; padding: 18px 24px 0 42px; color: var(--ink-white); }
  .service + .service { border-left: 2px solid #e4e2e2; padding-left: 28px; }
  .service--individual { width: 309px; background: var(--col-light); }
  .service--workshop { width: 310px; background: var(--col-mid); }
  .service--modules { width: 308px; background: var(--col-dark); }
  .service-title { margin: 0; font-family: "PT Sans Narrow", sans-serif; font-weight: 400; font-size: 28px; line-height: 30px; white-space: nowrap; }
  .service-sub { display: block; font-size: 13px; line-height: 14px; }
  .service-text { margin: 16px 0 0; font-family: "PT Sans Narrow", sans-serif; font-size: 16px; line-height: 20px; text-align: justify; hyphens: auto; color: var(--col-text); }

  .footer { position: absolute; left: 0; top: 1070px; width: 927px; height: 130px; background: var(--footer); color: var(--footer-text); }
  .brand { position: absolute; left: 44px; top: 24px; display: flex; align-items: center; }
  .brand-mark { width: 48px; height: 58px; background: var(--badge); }
  .brand-name { margin-left: 13px; font-size: 14px; line-height: 18px; }
  .brand-name .big { display: block; font-size: 22px; line-height: 26px; }
  .portrait { position: absolute; left: 310px; top: 6px; width: 95px; height: 95px; border-radius: 50%; background: radial-gradient(circle at 50% 45%, #c9a58a, #6a3a2a 70%, #3a2218); }
  .mentor { position: absolute; left: 415px; top: 30px; }
  .mentor-name { margin: 0; font-weight: 400; font-size: 26px; line-height: 30px; }
  .mentor-role { font-size: 12px; line-height: 16px; }
  .contact { position: absolute; left: 660px; top: 30px; font-size: 16px; }
  .contact-line { display: flex; align-items: center; height: 26px; white-space: nowrap; }
  .contact-icon { width: 20px; margin-right: 8px; font-weight: 700; font-size: 19px; }
  .contact-phone { font-weight: 700; letter-spacing: 3px; font-size: 18px; }
</style>
</head>
<body>
  <section class="hero">
    <div class="hero-scene" role="img" aria-label="Silhouetted team seated around a boardroom table against a sunset window"></div>
    <h1 class="hero-title">
      <span class="kicker">A STRENGTH-BASED APPROACH TO</span>
      <span class="main">MANAGING TEAM EFFECTIVENESS</span>
    </h1>
    <div class="promise">
      <h2 class="promise-heading">WE HELP<br>TEAMS GROW STRONGER BY</h2>
      <ul class="promise-list">
        <li>Bringing a deep awareness of their strengths and the strengths of their associates.</li>
        <li>Increasing the Team’s communication and sense of partnership.</li>
        <li>Improving employee engagement and effectiveness.</li>
      </ul>
    </div>
  </section>

  <section class="services">
    <article class="service service--individual">
      <h3 class="service-title">INDIVIDUAL<span class="service-sub">SESSIONS</span></h3>
      <p class="service-text">Conversational feedback and coaching sessions based on Brinmore TalentsFinder assessments. These sessions last about an hour and lead to a personalized translation of the results and how their strengths show up in their work and inherent blind spots they bring.</p>
    </article>
    <article class="service service--workshop">
      <h3 class="service-title">STRENGTH DISCOVERY<span class="service-sub">WORKSHOP</span></h3>
      <p class="service-text">A retreat-style Team Workshop in which the team learns each other’s unique Top 5 strengths. The session is very interactive and provides a common language that leads to improved communication and effectiveness. Tailored in 2.3.and 4-hour options are tailored to your Team’s challenges and opportunities.</p>
    </article>
    <article class="service service--modules">
      <h3 class="service-title">FOLLOW-ON<span class="service-sub">MODULES</span></h3>
      <p class="service-text">Follow-on is important to make the insights learned to be practical and integrated into the Teams’ approach and workflows. In a debrief session included as part of the workshop, we provide several 15-minute exercise modules for use in regular meetings, and we offer guest facilitated modules of 30- 60 minutes each.</p>
    </article>
  </section>

  <footer class="footer">
    <div class="brand">
      <div class="brand-mark"></div>
      <div class="brand-name">BRINMORE ACCREDITED<span class="big">Talents Mentor</span></div>
    </div>
    <div class="portrait" role="img" aria-label="Portrait photo of the mentor"></div>
    <div class="mentor">
      <h4 class="mentor-name">Warren Castellane</h4>
      <div class="mentor-role">Brinmore Workplace Talents Mentor</div>
    </div>
    <div class="contact">
      <div class="contact-line"><span class="contact-icon">@</span>warren@mentorIQ.example</div>
      <div class="contact-line">
        <span class="contact-icon">
          <svg width="16" height="18" viewBox="0 0 16 18" aria-hidden="true"><path d="M4 1 L7 5 L5 7 Q6 11 9 13 L11 11 L15 14 L13 17 Q4 16 1 4 Z" fill="none" stroke="#6a6a6a" stroke-width="1.8" stroke-linejoin="round"/></svg>
        </span>
        <span class="contact-phone">555-014-2270</span>
      </div>
    </div>
  </footer>
</body>
</html>
```